Brochure for Community-Based Therapy Company

Will be given out to patients, doctors, case managers. We are redesigning our marketing materials and would like a design for a brochure. We provide therapy to individuals who have been injured in car accidents or on the job. We provide occupational therapy, speech therapy and psychotherapy. We would like the brochure to utilize our corporate ID and color scheme that we are using for our other materials (see attached letterhead and logo).

Stock photos that are used should stay away from images of outpatient or hospital settings, stay away from photos with obvious disabilities (wheelchairs, learning to walk, etc), and nothing that looks like physical therapy, as we don't provide physical therapy only OT, Speech and psychotherapy. Would prefer to not have people wearing masks, as we will use this beyond the pandemic. Also, our staff wears business casual clothing so would prefer photos that the individuals are not wearing scrubs or other medical attire (lab coats, etc).

Target Market(s)

Patients, Physicians/Doctors, Case Managers

Industry/Entity Type

Healthcare

Requirements
Must have
• Prefer a booklet format but doesn't have to be 8.5 inch by 11 inch (can be a little smaller).

```html
<!DOCTYPE html>
<html lang="en">
<head>
<meta charset="utf-8">
<title>Evergreen Recovery Partners – Brochure Inner Spread</title>
<link href="https://fonts.googleapis.com/css2?family=Arimo:wght@400;700&display=swap" rel="stylesheet">
<style>
  :root {
    --paper: #f8f8f8;
    --paper-shade: #efefef;
    --ink: #2a2a2a;
    --sage: #8fa091;
    --sage-dark: #6f7f71;
    --rule: #d9dcd9;
  }
  * { margin: 0; padding: 0; box-sizing: border-box; }
  html, body { width: 1200px; height: 927px; overflow: hidden; }
  body {
    font-family: "Arimo", Arial, sans-serif;
    color: var(--ink);
    background: radial-gradient(ellipse at 60% 45%, var(--paper-shade) 0%, var(--paper) 60%);
  }
  .spread { position: relative; width: 1200px; height: 927px; }

  .section-head { position: absolute; display: flex; align-items: center; gap: 6px; }
  .section-head svg { width: 27px; height: 27px; }
  .section-title { font-size: 16.5px; font-weight: 700; color: var(--sage); letter-spacing: 0.1px; padding-top: 8px; }
  .rule { position: absolute; height: 1px; background: var(--rule); }

  .body-copy { position: absolute; font-size: 12.6px; line-height: 15.3px; }
  .body-copy p + p { margin-top: 15.3px; }

  .sub-title { position: absolute; font-size: 12.8px; font-weight: 700; color: var(--sage); }

  .list { position: absolute; list-style: none; font-size: 12.6px; line-height: 15.3px; }
  .list li { position: absolute; left: 0; white-space: nowrap; }
  .list li.wrap { white-space: normal; }
  .list li::before {
    content: ""; position: absolute; left: -11px; top: 4px;
    width: 5px; height: 5px;
    border-right: 2px solid var(--sage-dark); border-top: 2px solid var(--sage-dark);
    transform: rotate(45deg);
  }
  .list.major li::before { left: -14px; top: 3.5px; width: 6px; height: 6px; border-width: 2.5px; }
</style>
</head>
<body>
<main class="spread">

  <!-- Left column -->
  <div class="section-head" style="left:41px; top:32px;">
    <svg viewBox="0 0 28 28" aria-hidden="true">
      <circle cx="14" cy="14" r="13" fill="none" stroke="#6f7f71" stroke-width="1"/>
      <circle cx="14" cy="14" r="3.2" fill="none" stroke="#444" stroke-width="1.2"/>
      <circle cx="14" cy="14" r="6" fill="none" stroke="#444" stroke-width="1.4" stroke-dasharray="2 1.6"/>
      <circle cx="14" cy="5" r="1" fill="#444"/><circle cx="14" cy="23" r="1" fill="#444"/>
      <circle cx="5" cy="14" r="1" fill="#444"/><circle cx="23" cy="14" r="1" fill="#444"/>
    </svg>
    <h2 class="section-title">Why Our Approach to Brain Injury is Unique</h2>
  </div>
  <div class="rule" style="left:0; top:67px; width:600px;"></div>

  <div class="body-copy" style="left:43px; top:76px; width:556px;">
    <p>In more traditional therapy settings such as programs using outpatient models, attempts are made to simulate functional activities, combined with more structured tasks, all performed within their clinic environment. However, the inability to generalize learning has been shown to be a reoccurring difficulty for individuals with Traumatic Brain Injury and can often manifest in cognitive inflexibility, which makes carryover of their learned skills to the real world, a challenge.</p>
    <p>Community-based treatment circumvents this difficulty by conducting therapy in the person’s home, school, workplace, or other settings within their community, such as a grocery store or at a post office. Clinicians are therefore able to witness first hand where a task is experiencing success or breaking down and can structure treatment accordingly. This allows for greater natural development of functional skills, with generalization issues no longer an obstacle toward meeting treatment goals.</p>
    <p>At Evergreen Recovery Partners we are committed to helping people recover their cognitive, physical and psycho social abilities following brain injury through intensive individual treatment which focuses on safety, skill building and increasing independence, community reintegration, and overall life satisfaction. Our treatment approach is two-fold, with emphasis not only on direct restoration of brain functions, but also on helping the individual learn compensatory strategies (e.g., internal mnemonics, organizational systems, self-cuing techniques) or acquire assistive devices (e.g., planners, electronic reminders). Such methods are designed to reduce the effects of real-world disability when there is enduring cognitive impairment, and are most effective when introduced within a person’s own relevant environments.</p>
  </div>

  <div class="section-head" style="left:41px; top:491px;">
    <svg viewBox="0 0 28 28" aria-hidden="true">
      <circle cx="14" cy="14" r="13" fill="none" stroke="#6f7f71" stroke-width="1"/>
      <circle cx="14" cy="10" r="3.2" fill="#333"/>
      <path d="M8.5 17.5c0-3 2.5-4.3 5.5-4.3s5.5 1.3 5.5 4.3z" fill="#333"/>
      <path d="M6 18.5c2 3 14 3 16 0" fill="none" stroke="#333" stroke-width="1.5"/>
    </svg>
    <h2 class="section-title">Who We Serve</h2>
  </div>
  <div class="rule" style="left:0; top:527px; width:600px;"></div>

  <ul class="list major" style="left:58px; top:540px; width:530px;">
    <li class="wrap" style="top:0; width:520px;">We treat adults and adolescents with a variety of diagnoses. We service home and community locations throughout Southeast and mid-Michigan</li>
    <li class="wrap" style="top:46px; width:520px;">Our therapists hold a variety of certifications and endorsements including CBIS (Certified Brain Injury Specialist), NeuroSwallow, and VoiceBoost.</li>
    <li style="top:92px;">Diagnoses can include:</li>
  </ul>
  <ul class="list" style="left:69px; top:657px; width:420px;">
    <li style="top:0;">Traumatic Brain Injury</li>
    <li style="top:26px;">Postconcussional Syndrome</li>
    <li style="top:52px;">Spinal Cord Injury</li>
    <li style="top:78px;">Post-traumatic Stress Disorder</li>
    <li style="top:100px;">Depression</li>
    <li style="top:126px;">Anxiety</li>
    <li style="top:151px;">Mood Disorders</li>
    <li class="wrap" style="top:174px; width:420px;">Musculoskeletal / Orthopedic injuries(ie. Spinal fractures/pathology, nerve injuries, pain)</li>
    <li style="top:215px;">Visual Impairments</li>
  </ul>

  <!-- Right column -->
  <ul class="list" style="left:663px; top:40px;">
    <li style="top:0;">Balance Disorders</li>
    <li style="top:26px;">Movement Disorders</li>
    <li style="top:50px;">Neuromuscular Pathologies</li>
    <li style="top:75px;">Dysphagia</li>
  </ul>
  <ul class="list major" style="left:651px; top:150px;">
    <li style="top:0;">Funding Sourcesinclude:</li>
  </ul>
  <ul class="list" style="left:662px; top:171px;">
    <li style="top:0;">No-Fault Auto Insurance</li>
    <li style="top:20px;">Workers Compensation Insurance</li>
    <li style="top:45px;">Some Commercial Health Insurance Carriers</li>
  </ul>

  <div class="section-head" style="left:632px; top:282px;">
    <svg viewBox="0 0 28 28" aria-hidden="true">
      <circle cx="14" cy="14" r="13" fill="none" stroke="#6f7f71" stroke-width="1"/>
      <circle cx="14" cy="10" r="3.6" fill="none" stroke="#333" stroke-width="2" stroke-dasharray="1.8 1"/>
      <circle cx="14" cy="10" r="1.2" fill="#333"/>
      <path d="M6 17c2 0 4 1 6 2h5c1 0 1 1.5 0 1.5h-4M6 20.5c3 1.5 7 2.5 10 1.5l6-3" fill="none" stroke="#333" stroke-width="1.3"/>
    </svg>
    <h2 class="section-title">Services Offered</h2>
  </div>
  <div class="rule" style="left:600px; top:318px; width:600px;"></div>

  <h3 class="sub-title" style="left:665px; top:326px;">Speech Language Pathology</h3>
  <div class="body-copy" style="left:665px; top:348px; width:528px;">
    <p>Speech &amp; Language Pathologists are trained in the rehabilitation of deficits/disorders in the areas of language, articulation, voice, fluency, and dysphagia, with an underlying knowledge base of the neurological and physiologic processes affecting each. Deficits in the areas of attention, memory, information processing and executive functioning can impact all of the areas that speech and language pathologists treat, and are addressed in all treatment goals.</p>
  </div>
  <h3 class="sub-title" style="left:665px; top:450px;">Services Include:</h3>

  <ul class="list" style="left:676px; top:472px; width:510px;">
    <li class="wrap" style="top:0; width:510px; left:-11px; text-indent:11px;">Immediate and Short-Term Memory: compensatory strategies, modification of the environment for increased functional memory.</li>
    <li style="top:45px;">Attention and concentration</li>
    <li class="wrap" style="top:72px; width:500px;">Expressive Language: ability to express ideas, verbally, or in written format, in a concise organized fashion.</li>
    <li style="top:117px;">Comprehension and Retention of Verbal and Written Language</li>
    <li class="wrap" style="top:146px; width:500px;">Information Processing: gradually increase in the length and complexity of information presented to allow the brain to take in and process more information at one time.</li>
    <li style="top:204px;">Word Retrieval and Thought Formulation for Verbal and Written Expression</li>
    <li style="top:233px;">Pragmatic Language/Social Communication</li>
    <li class="wrap" style="top:263px; width:510px;">Executive Functioning: The mental processes that enable individuals to plan, focus attention, retain instructions, and juggle multiple tasks successfully. Assist with planning, initiating, carrying out tasks, as well as assist with self-monitoring and awareness for carryover of strategies.</li>
    <li style="top:338px;">Articulation</li>
    <li style="top:365px;">Dysarthria (lack of voluntary control)</li>
    <li style="top:394px;">Dysphagia (swallowing disorders)</li>
  </ul>

</main>
</body>
</html>
```